Game, Voice & Dedicated Server Company Needs a Business Card Design

We need a new business card design, centered around our new logo (PSD provided below).

Designs that we do like:
https://pixelmarsh.net/item/corporate-business-card/5382017?s_rank=43 (needs to be made more eye catching)

Our main areas of business are:
- Dedicated Servers
- Game Servers
- Voice Servers
- Mitigation Security Specialists

Industry/Entity Type

Business

Contact Information for Business Card

On the card: (and anything else you would suggest)
- Staff member name
- Staff member position in company
- Staff member phone number
- Staff member email
- Other / Staff member chat handle (plain icon)
- Website link

Colors
9bcb3c
abd036

Requirements
Must have
• Design of Card:
• - Green (same green as the logo)
• - Business / Corporate design
• - Something a little different / abstract that shouts premium

```html
<!DOCTYPE html>
<html lang="en">
<head>
<meta charset="utf-8">
<title>Tidewire Business Card</title>
<link href="https://fonts.googleapis.com/css2?family=Roboto:wght@400;500;700&display=swap" rel="stylesheet">
<style>
  :root {
    --green: #9bcb3c;
    --green-light: #abd036;
    --black: #0b0b0b;
    --paper: #ececea;
    --white: #ffffff;
    --backdrop: #b9b9b7;
  }
  * { box-sizing: border-box; margin: 0; padding: 0; }
  html, body { width: 1200px; height: 960px; overflow: hidden; }
  body {
    background: var(--backdrop);
    font-family: "Roboto", Arial, sans-serif;
    display: flex;
    flex-direction: column;
    align-items: center;
    justify-content: center;
    gap: 40px;
  }
  .card {
    width: 700px;
    height: 400px;
    position: relative;
    overflow: hidden;
    box-shadow: 0 10px 28px rgba(0,0,0,.25);
  }

  /* Back of card */
  .card-back { background: var(--black); }
  .card-back .brand {
    position: absolute; left: 0; right: 0; top: 96px;
    display: flex; flex-direction: column; align-items: center; gap: 18px;
  }
  .brand-square {
    width: 46px; height: 46px; background: var(--green);
  }
  .brand-name {
    font-weight: 700; color: var(--green);
    font-size: 54px; letter-spacing: -1px; line-height: 1;
  }
  .card-back .band {
    position: absolute; left: 0; right: 0; bottom: 0; height: 118px;
    background: var(--green-light);
    display: flex; align-items: center; justify-content: center;
  }
  .band .site {
    color: #f2f7e4; font-size: 22px; letter-spacing: 2px; font-weight: 400;
  }

  /* Front of card */
  .card-front { background: var(--paper); display: flex; }
  .front-brand-panel {
    width: 336px; height: 100%; position: relative;
    display: flex; flex-direction: column; align-items: center; justify-content: center; gap: 14px;
  }
  .accent-bar {
    position: absolute; left: 14px; top: 40px; bottom: 40px; width: 12px;
    background: var(--green); border-radius: 6px;
  }
  .front-brand-panel .brand-square { width: 40px; height: 40px; }
  .front-brand-panel .brand-name { font-size: 46px; }

  .contact-panel {
    flex: 1; background: var(--black); color: var(--white);
    padding: 30px 0 0 36px;
    display: flex; flex-direction: column; gap: 16px;
  }
  .contact-row { display: flex; align-items: center; gap: 20px; }
  .icon {
    width: 34px; height: 34px; flex: none;
    border-radius: 50%; border: 3px solid var(--green);
    background: var(--black);
    display: flex; align-items: center; justify-content: center;
  }
  .icon svg { width: 18px; height: 18px; }
  .contact-text { font-size: 18px; line-height: 1.2; }
  .staff-name { font-size: 22px; font-weight: 700; }
  .staff-position { font-size: 17px; }
</style>
</head>
<body>

  <section class="card card-back" aria-label="Business card back">
    <div class="brand">
      <div class="brand-square"></div>
      <div class="brand-name">TIDEWIRE</div>
    </div>
    <div class="band"><span class="site">www.tidewire.com</span></div>
  </section>

  <section class="card card-front" aria-label="Business card front">
    <div class="front-brand-panel">
      <div class="accent-bar"></div>
      <div class="brand-square"></div>
      <div class="brand-name">TIDEWIRE</div>
    </div>

    <div class="contact-panel">
      <div class="contact-row">
        <span class="icon"><svg viewBox="0 0 20 20" fill="#ffffff"><circle cx="10" cy="6" r="4"/><path d="M2 19c0-5 3.5-7 8-7s8 2 8 7z"/></svg></span>
        <div class="contact-text"><div class="staff-name">Staff's Name</div><div class="staff-position">Staff's Position</div></div>
      </div>
      <div class="contact-row">
        <span class="icon"><svg viewBox="0 0 20 20" fill="#ffffff"><path d="M10 1a6 6 0 0 0-6 6c0 5 6 12 6 12s6-7 6-12a6 6 0 0 0-6-6zm0 8.5A2.5 2.5 0 1 1 10 4.5a2.5 2.5 0 0 1 0 5z"/></svg></span>
        <div class="contact-text">Staff's Address<br>goes here</div>
      </div>
      <div class="contact-row">
        <span class="icon"><svg viewBox="0 0 20 20" fill="#ffffff"><path d="M5 2l3 4-2 2c1 2.5 3.5 5 6 6l2-2 4 3-2 3C9 17 3 11 2 5z"/></svg></span>
        <div class="contact-text">0123456789</div>
      </div>
      <div class="contact-row">
        <span class="icon"><svg viewBox="0 0 20 20" fill="none" stroke="#ffffff" stroke-width="2"><rect x="2" y="4" width="16" height="12"/><path d="M2 4l8 7 8-7"/></svg></span>
        <div class="contact-text">staffname@tidewire.com</div>
      </div>
      <div class="contact-row">
        <span class="icon"><svg viewBox="0 0 20 20" fill="#ffffff"><path d="M3 3h14v10H8l-4 4v-4H3z"/></svg></span>
        <div class="contact-text">Staff.Name</div>
      </div>
      <div class="contact-row">
        <span class="icon"><svg viewBox="0 0 20 20" fill="none" stroke="#ffffff" stroke-width="1.6"><circle cx="10" cy="10" r="8"/><ellipse cx="10" cy="10" rx="3.5" ry="8"/><path d="M2 10h16M3.5 5.5h13M3.5 14.5h13"/></svg></span>
        <div class="contact-text">www.tidewire.com</div>
      </div>
    </div>
  </section>

</body>
</html>
```